Business card for wedding & event planning company

I'm looking for a well designed double sided business card to represent my wedding and event planning company.

It should include the fact we manage the following events:
Weddings, birthdays, conferences, product launches, fashion shows & conventions
in the following areas:
Wiltshire, Oxfordshire, Berkshire & London

My contact details to be included are:

Moira Pennock
07715 482036
moira@amberlarkcelebrations.co.uk
www.amberlarkcelebrations.co.uk

My logo can be found at the following Filevaultex location:
AI file: https://www.filevaultex.com/s/k4mprt8wn31b7hz/brandlogo_sourcefile.ai?dl=0
PNG file:
https://www.filevaultex.com/s/h9qsle2vbx07mnd/brandlogo_image.png?dl=0

Target Market(s)

women aged 30-55

Industry/Entity Type

Wedding

Contact Information for Business Card

in the following areas:

Moira Pennock
Event Planner
07715 482036

Font styles to use
Serif
Sans Serif
Script

Requirements
Must have
• Purple and white colour scheme
Should not have
• Black background
• Please don't submit any of the see-through business card designs.

```html
<!DOCTYPE html>
<html lang="en">
<head>
<meta charset="utf-8">
<title>Amber Lark Celebrations – Business Card</title>
<link rel="stylesheet" href="https://fonts.googleapis.com/css2?family=Cormorant+Garamond:ital,wght@0,500;1,500&family=Great+Vibes&display=swap">
<style>
  :root {
    --page-bg: #ece9ee;
    --purple-deep: #8a1fa3;
    --purple-mid: #b23fcf;
    --purple-light: #cd6fe2;
    --purple-ink: #9a2fb8;
    --white: #ffffff;
    --rule-light: rgba(255, 255, 255, 0.75);
    --rule-grey: #c9c2cc;
    --card-shadow: 0 14px 30px rgba(60, 20, 70, 0.22);
  }
  * { box-sizing: border-box; margin: 0; padding: 0; }
  html, body {
    width: 1200px;
    height: 900px;
    overflow: hidden;
    background: var(--page-bg);
  }
  .canvas {
    width: 1200px;
    height: 900px;
    display: flex;
    flex-direction: column;
    align-items: center;
    justify-content: center;
    gap: 56px;
  }
  .card {
    position: relative;
    width: 630px;
    height: 360px;
    border-radius: 4px;
    box-shadow: var(--card-shadow);
    overflow: hidden;
    font-family: "Cormorant Garamond", Georgia, serif;
  }

  /* Front */
  .card--front {
    background: linear-gradient(120deg, var(--purple-deep) 0%, var(--purple-mid) 45%, var(--purple-light) 70%, var(--purple-mid) 100%);
    color: var(--white);
  }
  .front-brand {
    position: absolute;
    left: 40px;
    top: 0;
    width: 260px;
    height: 100%;
    display: flex;
    flex-direction: column;
    align-items: center;
    justify-content: center;
    gap: 18px;
  }
  .brand-mark {
    width: 58px;
    height: 58px;
    border: 2px solid var(--white);
    border-radius: 50%;
  }
  .brand-name {
    font-size: 34px;
    font-weight: 500;
    letter-spacing: 0.04em;
    text-align: center;
    line-height: 1.05;
    color: var(--white);
  }
  .front-divider {
    position: absolute;
    left: 320px;
    top: 70px;
    width: 1px;
    height: 220px;
    background: var(--rule-light);
  }
  .contact {
    position: absolute;
    left: 346px;
    top: 92px;
    right: 20px;
  }
  .contact-name {
    font-family: "Great Vibes", cursive;
    font-size: 44px;
    font-weight: 400;
    line-height: 1;
    margin-bottom: 20px;
  }
  .contact-list { list-style: none; }
  .contact-item {
    display: flex;
    align-items: center;
    gap: 9px;
    font-size: 16px;
    font-weight: 500;
    line-height: 1.75;
    white-space: nowrap;
  }
  .contact-icon { width: 13px; height: 13px; flex: none; }

  /* Back */
  .card--back {
    background: var(--white);
    color: var(--purple-ink);
  }
  .back-brand {
    position: absolute;
    top: 40px;
    left: 0;
    right: 0;
    display: flex;
    align-items: center;
    justify-content: center;
    gap: 20px;
  }
  .back-brand .brand-mark { border-color: var(--purple-ink); width: 64px; height: 64px; }
  .back-brand .brand-name { color: var(--purple-ink); font-size: 40px; }
  .back-divider {
    position: absolute;
    top: 150px;
    left: 150px;
    right: 150px;
    height: 1px;
    background: var(--rule-grey);
  }
  .services {
    position: absolute;
    top: 172px;
    left: 30px;
    right: 30px;
    text-align: center;
  }
  .services-title {
    font-size: 19px;
    font-weight: 500;
    letter-spacing: 0.08em;
    margin-bottom: 6px;
  }
  .services-list {
    font-size: 17px;
    font-style: italic;
    font-weight: 500;
  }
  .areas-band {
    position: absolute;
    left: 0;
    right: 0;
    bottom: 0;
    height: 48px;
    background: var(--purple-ink);
    color: var(--white);
    display: flex;
    align-items: center;
    justify-content: center;
    font-size: 19px;
    font-weight: 500;
    letter-spacing: 0.02em;
  }
</style>
</head>
<body>
<main class="canvas">
  <section class="card card--front" aria-label="Business card front">
    <div class="front-brand">
      <span class="brand-mark" aria-hidden="true"></span>
      <p class="brand-name">Amber Lark<br>Celebrations</p>
    </div>
    <span class="front-divider" aria-hidden="true"></span>
    <div class="contact">
      <h1 class="contact-name">Moira Pennock</h1>
      <ul class="contact-list">
        <li class="contact-item">
          <svg class="contact-icon" viewBox="0 0 16 16" aria-hidden="true"><path fill="#fff" d="M3.6 1.2l2.3 2.6-1.3 1.9c.9 2 2.6 3.7 4.6 4.6l1.9-1.3 2.6 2.3-1.4 2.3C7 13.6 2.4 9 1.4 2.6z"/></svg>
          07715 482036
        </li>
        <li class="contact-item">
          <svg class="contact-icon" viewBox="0 0 16 16" aria-hidden="true"><rect x="1" y="3" width="14" height="10" fill="#fff"/><path d="M1 3l7 6 7-6" fill="none" stroke="#a33bc2" stroke-width="1.4"/></svg>
          moira@amberlarkcelebrations.co.uk
        </li>
        <li class="contact-item">
          <svg class="contact-icon" viewBox="0 0 16 16" aria-hidden="true"><circle cx="8" cy="8" r="6.5" fill="none" stroke="#fff" stroke-width="1.5"/><ellipse cx="8" cy="8" rx="2.8" ry="6.5" fill="none" stroke="#fff" stroke-width="1.2"/><path d="M1.5 8h13" stroke="#fff" stroke-width="1.2"/></svg>
          www.amberlarkcelebrations.co.uk
        </li>
      </ul>
    </div>
  </section>

  <section class="card card--back" aria-label="Business card back">
    <div class="back-brand">
      <span class="brand-mark" aria-hidden="true"></span>
      <p class="brand-name">Amber Lark<br>Celebrations</p>
    </div>
    <span class="back-divider" aria-hidden="true"></span>
    <div class="services">
      <h2 class="services-title">WE MANAGE</h2>
      <p class="services-list">Weddings, birthdays, conferences, product launches, fashion shows &amp; conventions</p>
    </div>
    <div class="areas-band">Wiltshire, Oxfordshire, Berkshire &amp; London</div>
  </section>
</main>
</body>
</html>
```